Harbor Hide Revival Product Label

We need a design for a label to be used on bottles of leather cleaner and conditioner products that will be used in curated kits. We would like it to incorporate our business logo as well as have an area that we can fill in later with the appropriate product name as needed. We would like to see designs that use shades of brown, but we are open to other colors often seen in leather. I am including the Harbor Hide business Logo below, however again we would prefer to have the label in various shades of browns, rather than the red and grey, more like the mock-up that I am also attaching.

*** I am attaching examples of the types of bottles that will be used. They vary in size from 8 oz to 16 oz. if you are designing a label for a spray bottle they are from 16-32 oz. ***

```html
<!DOCTYPE html>
<html lang="en">
<head>
<meta charset="utf-8">
<title>Harbor Hide Revival – Leather Cleaner &amp; Conditioner Label</title>
<link rel="stylesheet" href="https://fonts.googleapis.com/css2?family=Noto+Serif:wght@400;500&display=swap">
<style>
  :root {
    --bg-peach: #dc9e8a;
    --bg-mid: #8a5a4c;
    --bg-deep: #2c1714;
    --label-rim: #a96f60;
    --label-rim-light: #c98e7c;
    --stitch-band: #3a1f1b;
    --panel-light: #b98273;
    --panel-dark: #7c4e43;
    --banner: #3b211d;
    --banner-edge: #2a1613;
    --accent-red: #7a1c1c;
    --ink: #ffffff;
    --stitch: #c48a7b;
  }
  html, body {
    margin: 0;
    padding: 0;
    width: 1144px;
    height: 1200px;
    overflow: hidden;
  }
  .canvas {
    position: relative;
    width: 1200px;
    height: 1259px;
    transform: scale(0.95333);
    transform-origin: 0 0;
    background:
      radial-gradient(ellipse 520px 420px at 1000px 560px, rgba(30,14,12,.95), rgba(30,14,12,0) 100%),
      radial-gradient(ellipse 700px 500px at 0px 0px, var(--bg-peach), rgba(220,158,138,0) 100%),
      radial-gradient(ellipse 600px 420px at 1200px 1259px, #b57a6b, rgba(181,122,107,0) 100%),
      linear-gradient(180deg, #b77c6b 0%, #6e4438 45%, #5a362d 60%, #9c6a5c 100%);
    font-family: "Noto Serif", Georgia, serif;
    color: var(--ink);
  }
  .label-art {
    position: absolute;
    inset: 0;
  }
  .text {
    position: absolute;
    margin: 0;
    white-space: nowrap;
    line-height: 1;
  }
  .brand-mark {
    position: absolute;
    left: 328px;
    top: 344px;
    width: 94px;
    height: 94px;
    border-radius: 50%;
    background: var(--ink);
  }
  .brand-name {
    left: 440px;
    top: 360px;
    font-size: 40px;
    font-weight: 500;
    letter-spacing: 1px;
  }
  .brand-sub {
    left: 441px;
    top: 407px;
    font-size: 15px;
    font-weight: 500;
    letter-spacing: 1px;
  }
  .tagline {
    left: 0;
    width: 1156px;
    text-align: center;
    top: 478px;
    font-size: 23px;
    letter-spacing: .5px;
  }
  .claim {
    left: 0;
    width: 1156px;
    text-align: center;
    top: 571px;
    font-size: 25px;
  }
  .product-name {
    left: 0;
    width: 1200px;
    text-align: center;
    top: 640px;
    font-size: 138px;
    letter-spacing: 1px;
  }
  .product-type {
    left: 0;
    width: 1156px;
    text-align: center;
    top: 812px;
    font-size: 34px;
  }
  .description {
    left: 0;
    width: 1156px;
    text-align: center;
    top: 872px;
    font-size: 23px;
    line-height: 30px;
  }
  .volume {
    left: 870px;
    top: 865px;
    font-size: 25px;
    transform: translate(-50%, -50%) rotate(90deg);
  }
</style>
</head>
<body>
<div class="canvas">
  <svg class="label-art" width="1200" height="1259" viewBox="0 0 1200 1259" aria-hidden="true">
    <defs>
      <linearGradient id="rimFill" x1="0" y1="0" x2="1" y2="1">
        <stop offset="0" stop-color="#9e6353"/>
        <stop offset=".45" stop-color="#c58b7a"/>
        <stop offset="1" stop-color="#a46a5b"/>
      </linearGradient>
      <radialGradient id="panelFill" cx=".55" cy=".25" r=".9">
        <stop offset="0" stop-color="#bd8676"/>
        <stop offset=".55" stop-color="#8d5a4d"/>
        <stop offset="1" stop-color="#b07868"/>
      </radialGradient>
      <radialGradient id="claimGlow" cx=".5" cy=".5" r=".5">
        <stop offset="0" stop-color="#8a1e1e"/>
        <stop offset=".7" stop-color="#7a1c1c" stop-opacity=".85"/>
        <stop offset="1" stop-color="#7a1c1c" stop-opacity="0"/>
      </radialGradient>
      <filter id="softShadow" x="-20%" y="-20%" width="140%" height="140%">
        <feDropShadow dx="0" dy="10" stdDeviation="14" flood-color="#1a0b09" flood-opacity=".55"/>
      </filter>
    </defs>

    <!-- outer rim -->
    <path filter="url(#softShadow)" fill="url(#rimFill)"
      d="M258 340 Q258 268 330 268 L560 268 C770 268 942 440 942 650 L942 940 Q942 1008 874 1008 L326 1008 Q258 1008 258 940 Z"/>
    <!-- dark stitched band -->
    <path fill="var(--stitch-band)"
      d="M280 345 Q280 290 335 290 L560 290 C758 290 920 452 920 650 L920 932 Q920 986 866 986 L334 986 Q280 986 280 932 Z"/>
    <!-- inner panel -->
    <path fill="url(#panelFill)"
      d="M298 350 Q298 308 340 308 L560 308 C748 308 902 462 902 650 L902 926 Q902 968 860 968 L340 968 Q298 968 298 926 Z"/>
    <!-- stitching -->
    <path fill="none" stroke="var(--stitch)" stroke-width="2" stroke-dasharray="16 12"
      d="M289 347 Q289 299 337 299 L560 299 C753 299 911 457 911 650 L911 929 Q911 977 863 977 L337 977 Q289 977 289 929 Z"/>

    <!-- divider with stars -->
    <line x1="352" y1="534" x2="528" y2="534" stroke="#fff" stroke-width="1.5" stroke-dasharray="6 3"/>
    <line x1="628" y1="534" x2="805" y2="534" stroke="#fff" stroke-width="1.5" stroke-dasharray="6 3"/>
    <polygon fill="#fff" points="549,527 551,532 557,532 552,535 554,541 549,537 544,541 546,535 541,532 547,532"/>
    <polygon fill="#fff" points="578,520 581,529 591,529 583,535 586,545 578,539 570,545 573,535 565,529 575,529"/>
    <polygon fill="#fff" points="607,527 609,532 615,532 610,535 612,541 607,537 602,541 604,535 599,532 605,532"/>

    <!-- claim glow -->
    <rect x="405" y="556" width="346" height="54" fill="url(#claimGlow)"/>

    <!-- product name banner -->
    <rect x="270" y="626" width="660" height="164" rx="8" fill="var(--banner-edge)"/>
    <rect x="278" y="633" width="644" height="150" rx="6" fill="none" stroke="#5a3630" stroke-width="1.5" stroke-dasharray="8 6"/>
    <rect x="286" y="640" width="628" height="138" rx="6" fill="var(--banner)"/>
  </svg>

  <div class="brand-mark"></div>
  <p class="text brand-name">HARBOR HIDE</p>
  <p class="text brand-sub">REVIVAL, INC</p>

  <p class="text tagline">PREMIUM LEATHER PRODUCT</p>
  <p class="text claim">Replaces Lost Oils</p>

  <h1 class="text product-name" style="font-weight:400">LEATHER</h1>

  <p class="text product-type">Cleaner &amp; Conditioner</p>
  <p class="text description">Lorem ipsum dolor sit amet,<br>consectetuer adipiscing elit, sed diam</p>
  <p class="text volume">6 FL OZ</p>
</div>
</body>
</html>
```